Flyer Design

Create a flyer using the logo theme. Single page for to be sent out on email. Attached is an image of the layout, below is the text. A5 and a4 versions.

Simplifying the MAZE

This short workshop is designed as a refresher for those surgeons who have attended a full Cox-MAZE training course, and wish to gain an update on the latest thinking with regards to the surgical treatment of Atrial Fibrillation.
We will start with an overview of the disease burden, talk to the foundation clinical evidence available, and cover the various lesion sets used by surgeons – with a view to simplifying the procedure. The workshop will also explain the technology used, how to treat the Left Atrial Appendage, the best ways to work with your EP colleagues, and involve a short hands-on session to familiarize you with the tools available to perform the Cox-MAZE procedure.

Faculty
{{image}}
Mr. Corwen Halse
Cardiothoracic Surgeon

Mr Halses training was completed at the Brannock Clinic, Rochester, Minnesota, between June 1995 and July 1997 followed by an advanced fellowship with Professor Osric J Talmane at the Westvale General Hospital. Additional expertise required visits to Belgium, Italy, England and the United States. Mr Halse now proctors internationally in order to share his knowledge and further improvement in all areas of minimal access and open cardiac and thoracic surgery.
Further overseas experience at the Westvale General Hospital in Canada culminated in the award of Clinical Fellowship in Cardiovascular Surgery in December 1997.

Mr Halse has contributed to many publications and is referee for Journal articles in very highly regarded professional journals. He performs both Cardiac surgery procedures and thoracic procedures at Harrowgate Private Hospital and Venholt Hospital, Melbourne. Mr Halse has performed in excess of 200 open Maze procedures and 35 via a Thoracoscopic approach.

Venue - TBA
Time : 5pm - 7.30pm, followed by dinner and case presentations

```html
<!DOCTYPE html>
<html lang="en">
<head>
<meta charset="utf-8">
<title>Simplifying the MAZE – Workshop Flyer</title>
<link href="https://fonts.googleapis.com/css2?family=Exo+2:wght@600;700&family=Ubuntu:wght@400;500;700&display=swap" rel="stylesheet">
<style>
  :root {
    --bg-dark: #1c1c1d;
    --bg-mid: #2e2f31;
    --bg-light: #3c3d40;
    --orange: #f58220;
    --blue: #1f8fd0;
    --text: #ffffff;
    --frame: #8a8a8a;
    --dark-text: #1e2a33;
  }
  * { margin: 0; padding: 0; box-sizing: border-box; }
  html, body { width: 846px; height: 1200px; overflow: hidden; background: var(--bg-dark); }
  .flyer {
    position: relative; width: 846px; height: 1200px; overflow: hidden;
    background: radial-gradient(ellipse at 50% 45%, var(--bg-light) 0%, var(--bg-mid) 45%, var(--bg-dark) 100%);
    font-family: "Ubuntu", sans-serif; color: var(--text);
  }
  .backdrop { position: absolute; inset: 0; }
  .title {
    position: absolute; top: 28px; left: 0; width: 100%; text-align: center;
    font-family: "Exo 2", sans-serif; font-weight: 700; font-size: 38px; color: var(--blue);
  }
  .title .accent { color: var(--orange); }
  .title .big { font-size: 44px; }
  .copy { font-size: 21px; line-height: 29px; text-align: justify; }
  .intro { position: absolute; left: 32px; width: 783px; top: 98px; }
  .intro p + p { margin-top: 29px; }
  .hl { color: var(--orange); }
  .num { color: var(--orange); font-size: 25px; }
  .faculty { position: absolute; left: 36px; top: 446px; width: 290px; text-align: center; }
  .faculty-label { color: var(--blue); font-weight: 700; font-size: 21px; margin-bottom: 6px; }
  .portrait {
    display: block; margin: 0 auto; width: 262px; height: 272px;
    border: 4px solid var(--frame);
    background: linear-gradient(160deg, #6f8fae 0%, #b9c3cc 55%, #3e4a56 100%);
  }
  .faculty-name { margin-top: 10px; color: var(--orange); font-weight: 700; font-size: 20px; line-height: 24px; }
  .faculty-role { color: var(--blue); font-weight: 700; font-size: 20px; line-height: 24px; }
  .bio-side { position: absolute; left: 344px; width: 471px; top: 456px; }
  .bio-full { position: absolute; left: 32px; width: 783px; top: 812px; }
  .bio-full p + p { margin-top: 29px; }
  .footer { position: absolute; left: 0; bottom: 0; width: 846px; height: 134px; }
  .venue {
    position: absolute; left: 0; top: 0; width: 200px; height: 134px; text-align: center;
    padding-top: 16px; padding-right: 40px;
  }
  .venue-label { font-family: "Exo 2", sans-serif; font-weight: 700; font-size: 26px; color: var(--text); }
  .venue-value { font-family: "Exo 2", sans-serif; font-weight: 700; font-size: 30px; color: var(--dark-text); margin-top: 8px; }
  .time { position: absolute; left: 200px; right: 0; top: 26px; text-align: center; font-family: "Exo 2", sans-serif; font-weight: 700; }
  .time-main { font-size: 32px; color: var(--text); }
  .time-sub { font-size: 25px; color: var(--dark-text); margin-top: 4px; }
</style>
</head>
<body>
<main class="flyer">
  <svg class="backdrop" width="846" height="1200" viewBox="0 0 846 1200" aria-hidden="true">
    <polygon points="0,560 40,610 0,660" fill="#4a4b4f" opacity="0.5"/>
    <polygon points="846,540 800,600 846,660" fill="#4a4b4f" opacity="0.5"/>
    <polygon points="0,0 846,0 846,12 0,12" fill="var(--orange)"/>
    <polygon points="670,0 846,0 846,12 660,12" fill="var(--blue)"/>
    <polygon points="0,1066 230,1066 190,1200 0,1200" fill="var(--blue)"/>
    <polygon points="200,1080 846,1080 846,1200 160,1200" fill="var(--orange)"/>
    <rect x="0" y="1078" width="846" height="3" fill="var(--blue)"/>
  </svg>

  <h1 class="title"><span class="accent">S</span>implifying the <span class="accent big">MAZE</span></h1>

  <section class="intro copy">
    <p>This short workshop is designed as a refresher for those surgeons who have attended a full <span class="hl">Cox-MAZE</span> training course, and wish to gain an update on the latest thinking with regards to the surgical treatment of Atrial Fibrillation.</p>
    <p>We will start with an overview of the disease burden, talk to the foundation clinical evidence available, and cover the various lesion sets used by surgeons – with a view to simplifying the procedure. The workshop will also explain the technology used, how to treat the Left Atrial Appendage, the best ways to work with your EP colleagues, and involve a short hands-on session to familiarize you with the tools available to perform the <span class="hl">Cox-MAZE</span> procedure.</p>
  </section>

  <aside class="faculty">
    <div class="faculty-label">Faculty</div>
    <div class="portrait" role="img" aria-label="Portrait photograph of Mr. Corwen Halse"></div>
    <div class="faculty-name">Mr. Corwen Halse</div>
    <div class="faculty-role">Cardiothoracic Surgeon</div>
  </aside>

  <p class="bio-side copy"><span class="hl">Mr Halses</span> training was completed at the Brannock Clinic, Rochester, Minnesota, between June 1995 and July 1997 followed by an advanced fellowship with Professor Osric J Talmane at the Westvale General Hospital. Additional expertise required visits to Belgium, Italy, England and the United States. Mr Halse now proctors internationally in order to share his knowledge and further improvement in all areas of minimal access and open cardiac and thoracic surgery.</p>

  <section class="bio-full copy">
    <p>Further overseas experience at the Westvale General Hospital in Canada culminated in the award of Clinical Fellowship in Cardiovascular Surgery in December 1997.</p>
    <p><span class="hl">Mr Halse</span> has contributed to many publications and is referee for Journal articles in very highly regarded professional journals. He performs both Cardiac surgery procedures and thoracic procedures at Harrowgate Private Hospital and Venholt Hospital, Melbourne. Mr Halse has performed in excess of <span class="num">200</span> open Maze procedures and <span class="num">35</span> via a Thoracoscopic approach.</p>
  </section>

  <footer class="footer">
    <div class="venue">
      <div class="venue-label">Venue :-</div>
      <div class="venue-value">TBA</div>
    </div>
    <div class="time">
      <div class="time-main">Time : 5pm - 7.30pm,</div>
      <div class="time-sub">Followed by Dinner and Case Presentations</div>
    </div>
  </footer>
</main>
</body>
</html>
```